Bright Oak Fitness Facility Business Cards

Business Card Design that incorporates the logo and tagline

Target Market(s)

Fitness, People Who Exercise

Contact Information for Business Card

2817 Mossgrove Bend Road
Tavares, Florida 32190
Phone: 352-555-Jump (5867)
www.brightoakfitness.example
info@brightoakfitness.example

Requirements
Must have
• Logo, Address, Website, email and tagline "More Than A Gym". Colors should be red/black/grey/white

```html
<!DOCTYPE html>
<html lang="en">
<head>
<meta charset="utf-8">
<title>Bright Oak Fitness – Business Card</title>
<link rel="stylesheet" href="https://fonts.googleapis.com/css2?family=Open+Sans:wght@400;600;700&display=swap">
<style>
  :root {
    --red: #d7262b;
    --black: #1c1c1c;
    --grey: #5a5a5a;
    --paper: #f4f4f4;
    --backdrop: #3a3a3c;
  }
  * { margin: 0; padding: 0; box-sizing: border-box; }
  html, body {
    width: 1200px; height: 900px; overflow: hidden;
    background: var(--backdrop);
    font-family: "Open Sans", sans-serif;
  }
  .card {
    position: absolute; left: 75px; top: 150px;
    width: 1050px; height: 600px;
    background: var(--paper);
    color: var(--grey);
  }
  .brand {
    position: absolute; left: 110px; top: 200px;
    width: 380px;
    display: flex; align-items: center; gap: 14px;
  }
  .brand-mark {
    width: 26px; height: 26px; border-radius: 50%;
    background: var(--red); flex: none;
  }
  .brand-name {
    font-size: 34px; font-weight: 700; letter-spacing: 1px;
    text-transform: uppercase; color: var(--black); line-height: 1.1;
  }
  .tagline {
    position: absolute; left: 110px; top: 360px;
    font-size: 30px; color: var(--red);
  }
  .contact {
    position: absolute; left: 580px; top: 190px; width: 440px;
  }
  .person-name {
    font-size: 44px; font-weight: 700; text-transform: uppercase;
    letter-spacing: 1px; line-height: 1;
  }
  .person-name .first { color: var(--red); }
  .person-name .last { color: var(--black); }
  .person-role { font-size: 28px; font-weight: 600; color: var(--grey); margin-top: 4px; }
  .rule { width: 170px; height: 2px; background: var(--red); margin: 14px 0; }
  .address { font-size: 25px; line-height: 1.3; }
  .channels { list-style: none; font-size: 25px; line-height: 1.4; }
  .channels li { display: flex; align-items: center; gap: 12px; }
  .channels svg { width: 20px; height: 20px; flex: none; }
</style>
</head>
<body>
  <section class="card">
    <div class="brand">
      <span class="brand-mark"></span>
      <span class="brand-name">Bright Oak Fitness</span>
    </div>
    <p class="tagline">More Than A Gym</p>

    <div class="contact">
      <h1 class="person-name"><span class="first">Dana</span> <span class="last">Whitfield</span></h1>
      <p class="person-role">President</p>
      <div class="rule"></div>
      <p class="address">2817 Mossgrove Bend Road<br>Tavares, Florida 32190</p>
      <div class="rule"></div>
      <ul class="channels">
        <li>
          <svg viewBox="0 0 20 20" aria-hidden="true"><path d="M5 2l3 4-2 2c1 2.5 3.5 5 6 6l2-2 4 3-2 3C9 18 2 11 2 4z" fill="var(--red)"/></svg>
          352-555-Jump (5867)
        </li>
        <li>
          <svg viewBox="0 0 20 20" aria-hidden="true"><rect x="1.5" y="4" width="17" height="12" fill="none" stroke="var(--red)" stroke-width="1.6"/><path d="M1.5 4l8.5 7 8.5-7" fill="none" stroke="var(--red)" stroke-width="1.6"/></svg>
          info@brightoakfitness.example
        </li>
        <li>
          <svg viewBox="0 0 20 20" aria-hidden="true"><g fill="none" stroke="var(--red)" stroke-width="1.4"><circle cx="10" cy="10" r="8"/><ellipse cx="10" cy="10" rx="3.5" ry="8"/><path d="M2 10h16M3.5 6h13M3.5 14h13"/></g></svg>
          www.brightoakfitness.example
        </li>
      </ul>
    </div>
  </section>
</body>
</html>
```